Business Card Design

A logo and business card design is required for a new podiatry business based on the Great Ocean Road, Victoria, Australia. The business will provide broad array of podiatry services to communities along the coast.

A distinctive design is sought that represents both professional allied health service delivery and the iconic location of the service, where the ocean meets the Otway ranges. Colours representative of the ocean blues, greens of the local forrest would be desirable.

Target Market(s)

GP's, other allied health professionals, members of the community with foot complaints

Industry/Entity Type

Health

Contact Information for Business Card

Tidewater Bend Podiatry
Gareth Linwell
B.Pod B App Sci (HM)
Phone: 0400 718 306
Email: tidewaterbendpodiatry@mailbrook.net

Requirements
Must have
• On the back of the card room allocated for appointment times.
Nice to have
• Would like the logo to incorporate a foot and the elements of the coast, whether it be ocean &/or the unique elements of the coast and the great ocean road.

```html
<!DOCTYPE html>
<html lang="en">
<head>
<meta charset="utf-8">
<title>Tidewater Bend Podiatry – Business Card</title>
<link href="https://fonts.googleapis.com/css2?family=Mulish:wght@600;700;800&display=swap" rel="stylesheet">
<style>
  :root {
    --ocean-blue: #29a9e1;
    --text-grey: #6b6b6b;
    --rule-grey: #6e6e6e;
    --sand-light: #ece6dc;
    --sand-mid: #e3d9cb;
    --shell-warm: #e6c7a4;
    --page: #ffffff;
  }
  * { margin: 0; padding: 0; box-sizing: border-box; }
  html, body {
    width: 1200px; height: 900px; overflow: hidden;
    background: var(--page);
    font-family: "Mulish", "Century Gothic", sans-serif;
  }
  .canvas { position: relative; width: 1200px; height: 900px; }

  .card {
    position: absolute;
    width: 520px; height: 300px;
    border: 9px solid var(--ocean-blue);
    overflow: hidden;
  }
  .card--front { left: 329px; top: 118px; }
  .card--back  { left: 331px; top: 491px; }

  .card__backdrop {
    position: absolute; inset: 0;
    background:
      radial-gradient(ellipse 170px 150px at 72% 48%, var(--shell-warm) 0%, rgba(230,199,164,0.35) 55%, rgba(230,199,164,0) 100%),
      linear-gradient(135deg, var(--sand-light) 0%, var(--sand-mid) 100%);
    opacity: 0.9;
  }
  .card__content { position: absolute; inset: 0; color: var(--text-grey); }

  /* Front */
  .front__mark {
    position: absolute; left: 211px; top: 42px;
    width: 72px; height: 72px; border-radius: 50%;
    background: var(--ocean-blue);
  }
  .front__name {
    position: absolute; left: 0; right: 0; top: 118px;
    text-align: center; font-weight: 700; font-size: 31px; line-height: 38px;
    letter-spacing: 0.2px;
  }
  .front__practitioner {
    position: absolute; left: 0; right: 0; top: 199px;
    text-align: center; font-weight: 700; font-size: 19px;
  }
  .front__contact {
    position: absolute; left: 0; right: 0; top: 248px;
    text-align: center; font-weight: 700; font-size: 12.5px;
  }
  .contact__label { color: var(--ocean-blue); }
  .contact__item + .contact__item { margin-left: 8px; }

  /* Back */
  .back__brand {
    position: absolute; left: 24px; top: 30px;
    display: flex; align-items: center; gap: 7px;
  }
  .back__mark {
    width: 40px; height: 40px; border-radius: 50%;
    background: var(--ocean-blue);
  }
  .back__name { font-weight: 700; font-size: 16px; line-height: 20px; }
  .back__title {
    position: absolute; left: 0; right: 0; top: 113px;
    text-align: center; font-weight: 700; font-size: 18px;
  }
  .appointment-field {
    position: absolute; left: 35px; width: 422px; height: 30px;
    border-bottom: 4px solid var(--rule-grey);
  }
  .appointment-field__label {
    position: absolute; right: 0; bottom: 1px;
    color: var(--ocean-blue); font-weight: 700; font-size: 14px;
  }
  .field--name { top: 133px; }
  .field--date { top: 172px; }
  .field--time { top: 212px; }
</style>
</head>
<body>
<main class="canvas">

  <section class="card card--front">
    <div class="card__backdrop" role="img" aria-label="Soft sandy beach background with seashells and a starfish"></div>
    <div class="card__content">
      <div class="front__mark" aria-hidden="true"></div>
      <h1 class="front__name">Tidewater Bend<br>Podiatry</h1>
      <p class="front__practitioner">Gareth Linwell B.Pod B App Sci (HM)</p>
      <p class="front__contact">
        <span class="contact__item"><span class="contact__label">Phone</span>: 0400 718 306</span>
        <span class="contact__item"><span class="contact__label">Email</span>: tidewaterbendpodiatry@mailbrook.net</span>
      </p>
    </div>
  </section>

  <section class="card card--back">
    <div class="card__backdrop" role="img" aria-label="Soft sandy beach background with seashells, a starfish and a sand dollar"></div>
    <div class="card__content">
      <div class="back__brand">
        <div class="back__mark" aria-hidden="true"></div>
        <p class="back__name">Tidewater Bend<br>Podiatry</p>
      </div>
      <h2 class="back__title">Appointment Reminder</h2>
      <div class="appointment-field field--name"><span class="appointment-field__label">Name</span></div>
      <div class="appointment-field field--date"><span class="appointment-field__label">Date</span></div>
      <div class="appointment-field field--time"><span class="appointment-field__label">Time</span></div>
    </div>
  </section>

</main>
</body>
</html>
```